GRape Crate Society Business Card design

Create a new business card that is contemporary but maintains the air of wine and the logo's history. I have put the original logo and a more current logo. The element we would like to keep intact is the visual the two gentleman holding the wine glasses...however, if there is an interesting interpretation of these two figures, have at it.

the company name is:

The Heritage Grape Crate Society
457 E. Larkspur Ave.
Fairhollow, CA 90327
800-555-0173

```html
<!DOCTYPE html>
<html lang="en">
<head>
<meta charset="utf-8">
<title>Grape Crate Society Business Card</title>
<link href="https://fonts.googleapis.com/css2?family=Montserrat:wght@500;600&family=Pirata+One&display=swap" rel="stylesheet">
<style>
  :root {
    --wine: #941c33;
    --wine-deep: #7d1529;
    --wine-soft: #b0566a;
    --paper: #ffffff;
    --backdrop: #d6d6d6;
  }
  * { box-sizing: border-box; margin: 0; padding: 0; }
  html, body { width: 1200px; height: 800px; overflow: hidden; }
  body {
    background: var(--backdrop);
    display: flex;
    align-items: center;
    justify-content: center;
    gap: 60px;
    font-family: "Montserrat", Arial, sans-serif;
  }
  .card {
    position: relative;
    overflow: hidden;
    background: var(--wine);
    box-shadow: 0 6px 18px rgba(0,0,0,0.18);
  }
  .card-front { width: 330px; height: 576px; }
  .card-back { width: 576px; height: 330px; }

  .card-front .vine-border {
    position: absolute;
    inset: 0;
    background: radial-gradient(ellipse at 50% 50%, var(--wine-soft) 0%, var(--wine) 60%, var(--wine-deep) 100%);
  }
  .card-front .oval {
    position: absolute;
    left: 50%;
    top: 50%;
    width: 316px;
    height: 540px;
    transform: translate(-50%, -50%);
    border-radius: 50%;
    background: var(--paper);
  }
  .card-front .content {
    position: absolute;
    inset: 0;
    display: flex;
    flex-direction: column;
    align-items: center;
    justify-content: center;
    color: var(--wine);
    text-align: center;
  }
  .brand { display: flex; flex-direction: column; align-items: flex-end; }
  .brand-name {
    font-weight: 600;
    font-size: 24px;
    line-height: 1.1;
    text-align: center;
    color: var(--wine);
  }
  .brand-phone {
    font-size: 10px;
    font-weight: 600;
    margin-top: 6px;
  }
  .person { margin-top: 34px; }
  .person-name {
    font-family: "Pirata One", "Times New Roman", serif;
    font-size: 24px;
    line-height: 1;
  }
  .person-role {
    font-size: 13px;
    font-weight: 500;
  }
  .contact {
    margin-top: 34px;
    font-size: 13px;
    font-weight: 500;
    line-height: 1.35;
  }
  .contact .phone { margin-top: 14px; font-size: 14px; }

  .card-back .emblem {
    position: absolute;
    left: 50%;
    top: 42%;
    width: 124px;
    height: 124px;
    transform: translate(-50%, -50%);
    border-radius: 50%;
    background: radial-gradient(circle, #f4e6ea 0%, var(--paper) 70%);
  }
</style>
</head>
<body>
  <section class="card card-front">
    <div class="vine-border" role="img" aria-label="White grapevine ornament border on wine red"></div>
    <div class="oval"></div>
    <div class="content">
      <div class="brand">
        <div class="brand-name">Grape Crate<br>Society</div>
        <div class="brand-phone">626-555-0148</div>
      </div>
      <div class="person">
        <div class="person-name">Daniel Reyes</div>
        <div class="person-role">Founder</div>
      </div>
      <div class="contact">
        <div>457 E. Larkspur Ave.</div>
        <div>Fairhollow, CA 90327</div>
        <div class="phone">800-555-0173</div>
      </div>
    </div>
  </section>

  <section class="card card-back">
    <div class="emblem" role="img" aria-label="Emblem illustration of two gentlemen raising wine glasses"></div>
  </section>
</body>
</html>
```